Business card design for new, innovative company - BluePlinth

We are a new company looking for a business card design that is fun, different and quirky. Must use corporate colour green - CMYK C:55, M:0, Y:100, K:0, and corporate colour grey - C:0, M:0, Y: 0, K:70.

We have developed the first real time data application, in which people are able to profile the data of their existing customers in order to pull out more good fit clients to direct their marketing activities at.

Industry/Entity Type

Marketing

Requirements
Must have
• Logo, name, title, telephone number, fax number, email, website, address

```html
<!DOCTYPE html>
<html lang="en">
<head>
<meta charset="utf-8">
<title>BluePlinth Business Card</title>
<link href="https://fonts.googleapis.com/css2?family=Mulish:wght@400;700;800&display=swap" rel="stylesheet">
<style>
  :root {
    --brand-green: #7cc242;
    --brand-grey: #6d6e71;
    --card-black: #0b0b0b;
    --pattern-dark: #1c1c1c;
    --text-white: #f2f2f2;
    --stage: #d9d9d6;
  }
  * { box-sizing: border-box; margin: 0; padding: 0; }
  html, body { width: 1200px; height: 1000px; overflow: hidden; }
  body {
    background: var(--stage);
    font-family: "Mulish", "Century Gothic", sans-serif;
    position: relative;
  }
  .card {
    position: absolute;
    width: 760px;
    height: 450px;
    border-radius: 34px;
    background: var(--card-black);
    overflow: hidden;
  }
  .card-front { left: 70px; top: 40px; }
  .card-back { left: 370px; top: 515px; }

  .grid-pattern {
    position: absolute;
    inset: 0;
    background: radial-gradient(circle at 50% 50%, #2a2a2a 0%, var(--pattern-dark) 70%);
  }
  .wordmark {
    position: absolute;
    display: flex;
    align-items: center;
    gap: 14px;
    font-weight: 800;
    color: var(--brand-green);
    letter-spacing: -2px;
  }
  .wordmark-mark {
    display: block;
    background: var(--brand-grey);
    border-radius: 6px;
  }
  .card-front .wordmark { left: 120px; top: 215px; font-size: 78px; }
  .card-front .wordmark-mark { width: 46px; height: 46px; }
  .card-back .wordmark { left: 50px; top: 30px; font-size: 58px; }
  .card-back .wordmark-mark { width: 34px; height: 34px; }

  .address {
    position: absolute;
    left: 60px;
    top: 205px;
    color: var(--text-white);
    font-size: 17px;
    line-height: 22px;
  }
  .address-label {
    color: var(--brand-green);
    font-weight: 700;
    font-size: 24px;
    margin-bottom: 12px;
  }
  .contact {
    position: absolute;
    right: 40px;
    bottom: 40px;
    text-align: right;
    color: var(--text-white);
    font-size: 16px;
    line-height: 21px;
  }
  .contact-name {
    color: var(--brand-green);
    font-weight: 700;
    font-size: 26px;
    margin-bottom: 10px;
  }
  .contact-line {
    display: flex;
    justify-content: flex-end;
    align-items: center;
    gap: 8px;
  }
  .contact-icon { width: 13px; height: 13px; flex: none; }
</style>
</head>
<body>

<section class="card card-front">
  <div class="grid-pattern" role="img" aria-label="Grid of grey rounded-square outlines covering the card"></div>
  <div class="wordmark"><span>BluePlinth</span><span class="wordmark-mark"></span></div>
</section>

<section class="card card-back">
  <div class="wordmark"><span>BluePlinth</span><span class="wordmark-mark"></span></div>

  <address class="address" style="font-style:normal">
    <div class="address-label">Address</div>
    22 Larkfield Road,<br>
    Elmsby,<br>
    Northvale,<br>
    EL4 2QT
  </address>

  <div class="contact">
    <div class="contact-name">Nadia Brennan</div>
    <div class="contact-line">07700900412
      <svg class="contact-icon" viewBox="0 0 13 13"><rect x="3" y="1" width="7" height="11" rx="1.5" fill="none" stroke="var(--brand-green)" stroke-width="1.4"/></svg>
    </div>
    <div class="contact-line">01632 960548
      <svg class="contact-icon" viewBox="0 0 13 13"><path d="M3 1.5 L5 4 L4 5.5 C5 7.5 6 8.5 7.5 9 L9 8 L11.5 10 L10 12 C5.5 11.5 1.5 7.5 1 3 Z" fill="var(--brand-green)"/></svg>
    </div>
    <div class="contact-line">nadia.brennan@plinthdata.com
      <svg class="contact-icon" viewBox="0 0 13 13"><rect x="1" y="3" width="11" height="7.5" fill="none" stroke="var(--brand-green)" stroke-width="1.3"/><path d="M1 3 L6.5 7.5 L12 3" fill="none" stroke="var(--brand-green)" stroke-width="1.3"/></svg>
    </div>
    <div class="contact-line">www.blueplinth.com
      <svg class="contact-icon" viewBox="0 0 13 13"><circle cx="6.5" cy="6.5" r="5.3" fill="none" stroke="var(--brand-green)" stroke-width="1.3"/><path d="M1.2 6.5 H11.8 M6.5 1.2 C4 4 4 9 6.5 11.8 M6.5 1.2 C9 4 9 9 6.5 11.8" fill="none" stroke="var(--brand-green)" stroke-width="1"/></svg>
    </div>
  </div>
</section>

</body>
</html>
```